WP website design (Vell)

We need a wordpress design for an established auction and real estate company based in Tennessee. The winning design will incorporate a professional color scheme with company logo in a clean layout. The design needs to consider that this will be developed on a responsive theme. Colors are those that will highlight the logo.

Industry/Entity Type

Real Estate

Font styles to use
Sans Serif

Colors

Designer to choose colors to be used in the design.

Requirements
Must have
• Navigation: 1) Home - with auctions as content as seen at http://quorvibidhouse.com/ 2) Current Auctions 3) Past Auctions 4) Referrals 5) Why Auction 6) About Us 7) Contact Us

Header will have logo, contact info, Social icons (Facebook, Twitter, Youtube) and tagline "Do Well, Ring Vell!' Slideshow (use stock real estate image for image) will be used either in header or content area.

Widgets: Email signup form, Upcoming Auctions, Register for Online Bidding text, testimonials

Footer will have contact info (below) smaller company logo, and the association logos attached.

```html
<!DOCTYPE html>
<html lang="en">
<head>
<meta charset="utf-8">
<title>Vell Realty &amp; Auction</title>
<link rel="stylesheet" href="https://fonts.googleapis.com/css2?family=Arimo:wght@400;700&family=Gelasio:wght@400&display=swap">
<style>
:root{
  --green:#6b8a3a;
  --green-light:#8fb04f;
  --navy:#4a4d73;
  --navy-dark:#3d4062;
  --ink:#222;
  --muted:#555;
  --page:#eceeef;
  --panel:#ffffff;
  --line:#cfd2d6;
  --footer:#f3f4f5;
  --strip:#e4e6e8;
  --sky:#c9d6e3;
  --sky-dark:#8fa6bf;
  --accent:#f2b640;
}
*{box-sizing:border-box;margin:0;padding:0}
html,body{width:704px;height:1200px;overflow:hidden}
body{position:relative;background:var(--page);font-family:Arimo,Arial,sans-serif;color:var(--ink);font-size:8px;line-height:1.3}
.abs{position:absolute}

/* header */
.site-header{left:0;top:0;width:704px;height:80px;background:linear-gradient(#f4f6f8,#e6eaee)}
.brand{left:62px;top:8px}
.brand-name{display:flex;align-items:center;gap:6px;font-weight:700;font-size:34px;color:var(--green);line-height:1}
.brand-mark{width:16px;height:16px;background:var(--green)}
.brand-sub{font-size:10px;color:var(--muted);margin-top:2px}
.brand-tag{font-size:10px;color:var(--ink);letter-spacing:.5px;margin-top:1px}
.firm{left:194px;top:10px;font-size:7px;color:var(--muted);writing-mode:vertical-rl}
.header-contact{left:522px;top:16px;font-size:7px;color:var(--ink)}
.header-contact .phone{font-size:14px;margin-top:6px}
.header-contact .phone span{color:var(--green)}

/* nav */
.main-nav{left:60px;top:80px;width:580px;height:26px;background:var(--navy);border-bottom:3px solid var(--green-light);display:flex}
.main-nav a{color:#fff;text-decoration:none;font-size:8px;padding:0 10px;line-height:26px;text-transform:uppercase}
.main-nav a.active{background:var(--green)}

/* hero */
.hero{left:60px;top:111px;width:580px;height:203px;background:linear-gradient(var(--sky) 0%,#e8eef3 55%,#7e9a5a 88%)}
.hero-photo{left:260px;top:20px;width:300px;height:170px;background:linear-gradient(#a9a49a,#8d8a82 60%,#5f7a45);border-radius:3px}
.hero-title{left:82px;top:170px;font-family:Gelasio,Georgia,serif;font-size:20px;color:#1f1f1f}
.hero-text{left:82px;top:194px;width:180px;font-size:10px;color:#222}
.dots{left:575px;top:292px;display:flex;gap:3px}
.dots i{width:5px;height:5px;border-radius:50%;background:#fff}
.dots i:first-child{background:var(--accent)}

/* call band */
.call-band{left:0;top:322px;width:704px;height:50px;background:var(--navy);color:#fff;font-size:20px;text-align:center;line-height:50px}
.call-band span{color:var(--accent)}

/* content */
.content{left:60px;top:386px;width:580px;height:656px;background:var(--panel)}
.section-title{font-size:17px;color:#222}
.auction{position:absolute;left:41px;width:317px}
.auction-bar{height:20px;background:var(--navy);color:#fff;font-size:12px;line-height:20px;padding-left:6px}
.auction-photo{position:absolute;left:0;top:26px;width:83px;height:85px;background:linear-gradient(#9cb4cc,#8b5a3a 55%,#5e7b3c)}
.auction-btns{position:absolute;left:8px;top:117px;width:64px}
.auction-btns div{height:14px;margin-bottom:5px;color:#fff;font-size:9px;text-align:center;line-height:14px}
.btn-details{background:var(--green)}
.btn-photos{background:var(--navy-dark)}
.btn-videos{background:#b5b8bd}
.summary{position:absolute;left:89px;top:29px;width:228px;height:58px;border:1px solid var(--line);padding:6px}
.summary h3{font-size:12px;font-weight:700;margin-bottom:4px}
.details{position:absolute;left:89px;top:95px;width:228px;height:187px;border:1px solid var(--line);padding:8px 14px}
.details h4{font-size:11px;font-weight:700;line-height:1.1}
.details p{margin:2px 0 7px}
.details b{font-weight:700}
.bid{display:inline-block;border:1px solid #aaa;background:linear-gradient(#fff,#e2e2e2);font-size:11px;padding:1px 12px;margin:2px 0 6px}
.pager{left:199px;top:640px;display:flex;gap:4px;align-items:center;font-size:8px}
.pager .btn{background:#d7d9dc;padding:1px 8px}
.pager .cur{background:var(--navy);color:#fff;padding:0 3px}

/* sidebar */
.side-title{font-size:13px;color:#222}
.search{left:391px;top:35px;display:flex;gap:3px}
.search .field{width:108px;height:17px;border:1px solid var(--line);color:#999;font-size:7px;padding:4px 6px}
.search .go{width:24px;height:17px;background:var(--green);color:#fff;font-size:9px;text-align:center;line-height:17px}
.upcoming{left:391px;top:92px;width:159px;height:150px;border:1px solid var(--line);text-align:center}
.upcoming h5{font-size:10px;color:#2f8a8a;font-weight:400;margin-top:8px}
.upcoming .thumb{width:94px;height:68px;margin:6px auto 8px;background:linear-gradient(#b9cbe0,#d3c7b3 55%,#6f8c4c);border:1px solid var(--line)}
.upcoming p{font-size:6px}
.testimonial{left:391px;top:285px;width:159px;height:79px;background:var(--green);color:#fff;font-style:italic;font-size:7.5px;padding:10px}
.client{left:391px;top:382px;width:159px;text-align:right;color:var(--green);font-size:10px}
.client small{display:block;color:#333;font-size:6px}
.news-text{left:391px;top:438px;width:160px;font-size:7.5px}
.input{width:124px;height:15px;border:1px solid var(--line);font-size:7px;color:#888;padding:3px 6px}
.submit{width:62px;height:17px;background:var(--navy);color:#fff;font-size:11px;text-align:center;line-height:17px}

/* footer */
.site-footer{left:0;top:1050px;width:704px;height:108px;background:var(--footer)}
.fcol h6{font-size:10px;font-weight:400;margin-bottom:5px}
.fcol li{list-style:none;font-size:6.5px;line-height:1.5}
.fbrand{left:553px;top:16px}
.fbrand .brand-name{font-size:20px}
.fbrand .brand-mark{width:10px;height:10px}
.social{left:553px;top:56px;display:flex;gap:4px}
.social i{width:15px;height:15px;background:#bcbec1}
.bottom-strip{left:0;top:1158px;width:704px;height:42px;background:var(--strip)}
.badges{left:72px;top:1164px;display:flex;gap:8px;align-items:center}
.badges i{height:26px;background:#bfc2c5}
.copy{left:470px;top:1170px;font-size:6.5px}
</style>
</head>
<body>

<header class="site-header abs">
  <div class="brand abs">
    <div class="brand-name">Vell<span class="brand-mark"></span></div>
    <div class="brand-sub">Realty &amp; Auction LLC</div>
    <div class="brand-tag">Do Well, Ring Vell!</div>
  </div>
  <div class="firm abs">FIRM # 4180</div>
  <div class="header-contact abs">
    123 Dummy Building 10th floor<br>Dummy Street<br>Dummy State United State
    <div class="phone">Ph.<span>555-014-2290</span></div>
    Email:info@vellbidhouse.com
  </div>
</header>

<nav class="main-nav abs">
  <a class="active">Home</a><a>Current Auctions</a><a>Past Auctions</a><a>Referrals</a><a>Why Auction</a><a>About Us</a><a>Contact Us</a>
</nav>

<section class="hero abs" role="img" aria-label="Slideshow photo of a large two-storey stone house under a cloudy sky">
  <div class="hero-photo abs"></div>
</section>
<h1 class="hero-title abs">Duis aute irure dolor</h1>
<p class="hero-text abs">Lorem ipsum dolor sit amet, consectetur adipiscing elit. Sed sit amet laoreet turpis.</p>
<div class="dots abs"><i></i><i></i><i></i><i></i><i></i></div>

<div class="call-band abs">Do Well, Ring Vell! <span>Call Now</span> 555 014 2290</div>

<main class="content abs">
  <h2 class="section-title abs" style="left:41px;top:18px">Upcoming Auctions</h2>

  <article class="auction" style="top:45px">
    <div class="auction-bar">This is Dummy Auction</div>
    <div class="auction-photo" role="img" aria-label="Photo of a log lodge home with trees"></div>
    <div class="auction-btns"><div class="btn-details">Details</div><div class="btn-photos">Photos</div><div class="btn-videos">Videos</div></div>
    <div class="summary"><h3>Dummy Auction</h3>Lorem ipsum dolor sit amet, consectetur adipiscing elit. Sed sit amet laoreet turpis.</div>
    <div class="details">
      <h4>Online Pre-Bidding</h4>
      <p><b>Began:</b> Saturday, June 28, 2014 at 4:00 PM EDT</p>
      <p style="margin-top:12px"><b>Ends:</b> Sunday, June 29, 2014 at 4:00 PM EDT</p>
      <h4>Live On-Site Auction with Online Bidding</h4>
      <p><b>Begins:</b> Thursday, May 24, 2018 at 6:00 AM EDT</p>
      <p style="margin-top:12px"><b>Ends:</b> Sunday, May 27, 2018 at 6:00 AM EDT</p>
      <span class="bid">Bid Online</span>
      <p><b>Location:</b><br>P.O. Box 40417<br>Fairbrook, VA 24990</p>
    </div>
  </article>

  <article class="auction" style="top:342px">
    <div class="auction-bar">This is Dummy Auction</div>
    <div class="auction-photo" role="img" aria-label="Photo of a log lodge home with trees"></div>
    <div class="auction-btns"><div class="btn-details">Details</div><div class="btn-photos">Photos</div><div class="btn-videos">Videos</div></div>
    <div class="summary"><h3>Dummy Auction</h3>Lorem ipsum dolor sit amet, consectetur adipiscing elit. Sed sit amet laoreet turpis.</div>
    <div class="details">
      <h4>Online Pre-Bidding</h4>
      <p><b>Began:</b> Saturday, June 28, 2014 at 4:00 PM EDT</p>
      <p style="margin-top:12px"><b>Ends:</b> Sunday, June 29, 2014 at 4:00 PM EDT</p>
      <h4>Live On-Site Auction with Online Bidding</h4>
      <p><b>Begins:</b> Thursday, May 24, 2018 at 6:00 AM EDT</p>
      <p style="margin-top:12px"><b>Ends:</b> Sunday, May 27, 2018 at 6:00 AM EDT</p>
      <span class="bid">Bid Online</span>
      <p><b>Location:</b><br>P.O. Box 40417<br>Fairbrook, VA 24990</p>
    </div>
  </article>

  <div class="pager abs"><span class="btn">Pre</span><span class="cur">1</span>2 3 4 5<span class="btn">Next</span></div>

  <aside>
    <h3 class="side-title abs" style="left:392px;top:16px">Auction Search</h3>
    <div class="search abs"><div class="field">Search Here...</div><div class="go">GO</div></div>
    <h3 class="side-title abs" style="left:392px;top:68px">Upcoming Auctions</h3>
    <div class="upcoming abs">
      <h5>Dummy Auction01</h5>
      <div class="thumb" role="img" aria-label="Photo of a large brick house"></div>
      <p>06/25/15 at 1:00 PM EDT<br>to<br>06/26/15 at 1:00 PM EDT</p>
    </div>
    <h3 class="side-title abs" style="left:392px;top:257px">Testimonials</h3>
    <div class="testimonial abs">Lorem ipsum dolor sit amet, consectetur adipiscing elit. Sed sit amet laoreet turpis. Integer aliquet gravida varius. Praesent in pretium tortor. Quisque eu quam vel quam suscipit varius.</div>
    <svg class="abs" style="left:520px;top:364px" width="16" height="10" viewBox="0 0 16 10"><path d="M0 0H16L14 10Z" fill="#6b8a3a"/></svg>
    <div class="client abs">Client name here<small>Dummy Place here</small></div>
    <h3 class="side-title abs" style="left:392px;top:413px">Newsletter Sign up</h3>
    <p class="news-text abs">Lorem ipsum dolor sit amet, consectetur adipiscing elit. Sed sit amet laoreet turpis.</p>
    <div class="input abs" style="left:391px;top:474px">Your Name</div>
    <div class="input abs" style="left:391px;top:499px">Email Address</div>
    <div class="submit abs" style="left:391px;top:525px">Submit</div>
  </aside>
</main>

<footer class="site-footer abs">
  <div class="fcol abs" style="left:65px;top:12px"><h6>Quick Link</h6><ul><li>Home</li><li>Current</li><li>Auctions</li><li>Past Auctions</li><li>Referrals</li><li>Why Auction</li><li>About Us</li></ul></div>
  <div class="fcol abs" style="left:146px;top:12px"><h6>Getting Started</h6><ul><li>Overview</li><li>Creating an Account</li><li>Register</li><li>Bid</li></ul></div>
  <div class="fcol abs" style="left:245px;top:12px"><h6>Buying</h6><ul><li>Residential</li><li>Foreclosure</li><li>Commercial</li><li>Notes</li><li>For Agents &amp; Brokers</li></ul></div>
  <div class="fcol abs" style="left:330px;top:12px"><h6>Selling</h6><ul><li>Commercial</li><li>For Agents &amp; Brokers</li></ul></div>
  <div class="fcol abs" style="left:422px;top:12px"><h6>Contact</h6><ul><li>123 Dummy Building 10th floor</li><li>Dummy Street</li><li>Dummy State United State</li><li>&nbsp;</li><li>Ph.555-014-2290</li><li>Email:info@vellbidhouse.com</li></ul></div>
  <div class="fbrand abs"><div class="brand-name">Vell<span class="brand-mark"></span></div></div>
  <div class="social abs"><i></i><i></i><i></i><i></i></div>
</footer>

<div class="bottom-strip abs"></div>
<div class="badges abs"><i style="width:50px"></i><i style="width:28px"></i><i style="width:62px"></i><i style="width:24px"></i></div>
<div class="copy abs">Copyright 2014vellbidhouse.com All Right Reserved.</div>

</body>
</html>
```